Business Card Design Project

I am a new business offering a consulting service in Homeware buying, product development and trend forecasting. I would like to use colours that are current and on trend now. Needs to be eye catching, speak of creativity and design.

Front: Matt charcoal card with black gloss embossing name print
Back: white with Pink text

Pink pantone: 812c

Target Market(s)

Retailers and Wholesalers of Homeware products

Industry/Entity Type

Business

Requirements
Must have
• Please go to this link and the card on this link is what I am looking for.

http://www.vistrafolio.net/gallery/Pre_formed-ID/582614

1. Card Front

Name on front of card: MARLOWE FINCH

2. Back card

The following text must be designed onto the card:

Address: 17 Lindel Street ,Paddington, 2021, NSW, Sydney, Australia
Mobile: +61 (0)412305687
Email: finchsyd@orvalink.net.au

Homeware trends
Product development and sourcing
Strategic Buying management
Nice to have
• Creativity in selection of font, composition and proportion.
Should not have
• I don't want to see graphics/shapes on the card.

```html
<!DOCTYPE html>
<html lang="en">
<head>
<meta charset="utf-8">
<title>Marlowe Finch – Business Card</title>
<link href="https://fonts.googleapis.com/css2?family=Audiowide&family=Arimo:wght@400;700&display=swap" rel="stylesheet">
<style>
  :root {
    --backdrop: #d9d9db;
    --pink: #e8489e;
    --pink-deep: #d63a8c;
    --charcoal: #212429;
    --ink: #111113;
  }
  html, body {
    margin: 0;
    padding: 0;
    overflow: hidden;
  }
  .canvas {
    width: 1200px;
    height: 880px;
    background: var(--backdrop);
    position: relative;
    overflow: hidden;
  }
  .card {
    position: absolute;
    top: 297px;
    width: 500px;
    height: 286px;
    box-sizing: border-box;
    box-shadow: 0 6px 18px rgba(0,0,0,0.18);
  }
  .card-back {
    left: 70px;
    background: var(--pink);
    color: var(--ink);
    padding: 42px 34px 0 40px;
    font-family: "Arimo", Arial, sans-serif;
  }
  .card-back .name {
    font-family: "Audiowide", sans-serif;
    font-size: 34px;
    margin: 0 0 10px 28px;
    letter-spacing: 0.5px;
  }
  .services {
    list-style: none;
    margin: 0 0 22px 36px;
    padding: 0;
    font-size: 13px;
    line-height: 17px;
  }
  .services li::before {
    content: "•";
    margin-right: 6px;
  }
  .contact {
    margin: 0 0 0 8px;
    font-size: 13px;
    line-height: 18px;
  }
  .contact p { margin: 0; }
  .contact .address { margin-left: 22px; }
  .card-front {
    left: 630px;
    background: var(--charcoal);
    border: 3px solid var(--pink);
    display: flex;
    align-items: center;
    justify-content: center;
  }
  .card-front .name {
    font-family: "Audiowide", sans-serif;
    font-size: 50px;
    color: var(--pink);
    letter-spacing: 1px;
    margin: 0;
    text-shadow: 1px 2px 0 var(--pink-deep), 2px 4px 4px rgba(0,0,0,0.55);
  }
</style>
</head>
<body>
<main class="canvas">
  <section class="card card-back">
    <h2 class="name">Marlowe Finch</h2>
    <ul class="services">
      <li>Homeware trends</li>
      <li>Product development and sourcing</li>
      <li>Strategic Buying management</li>
    </ul>
    <div class="contact">
      <p class="address">17 Lindel Street ,Paddington, 2021, NSW, Sydney, Australia</p>
      <p>m: +61 (0)412305687</p>
      <p>e: finchsyd@orvalink.net.au</p>
    </div>
  </section>
  <section class="card card-front">
    <h1 class="name">Marlowe Finch</h1>
  </section>
</main>
</body>
</html>
```